Commercial Real Estate

We need a business card design for a new commercial real estate business that specializes in apartment building brokerage. Not individual units but the entire complex. We find and represent the owners existing buildings and well as new buyers for those buildings. The design should convey trust, integrity, knowledge and growth. It should be easily read.

Target Market(s)

40 to 65 years old

Industry/Entity Type

Real Estate

```html
<!DOCTYPE html>
<html lang="en">
<head>
<meta charset="utf-8">
<title>Keyrise Property Investments – Business Card</title>
<link href="https://fonts.googleapis.com/css2?family=Open+Sans:wght@400;600&display=swap" rel="stylesheet">
<style>
  :root {
    --backdrop: #e4e6e5;
    --card: #ffffff;
    --teal: #5fbfb8;
    --slate: #6f8c8a;
    --ink: #3d4a4a;
    --name: #3f7c7a;
    --rule: #9aa5a4;
  }
  * { box-sizing: border-box; margin: 0; padding: 0; }
  html, body {
    width: 1200px; height: 899px; overflow: hidden;
    background: var(--backdrop);
    font-family: "Open Sans", Arial, sans-serif;
    color: var(--ink);
  }
  .card {
    position: absolute; left: 150px; top: 185px;
    width: 900px; height: 530px;
    background: var(--card);
    border-radius: 48px;
    overflow: hidden;
    box-shadow: 0 12px 30px rgba(0,0,0,0.12);
  }
  .card__swoosh { position: absolute; inset: 0; }
  .brand {
    position: absolute; left: 70px; top: 160px;
    display: flex; align-items: center; gap: 14px;
  }
  .brand__mark { width: 22px; height: 22px; background: var(--teal); }
  .brand__name {
    font-weight: 600; font-size: 46px; letter-spacing: 3px;
    color: var(--slate); line-height: 1;
  }
  .brand__tagline {
    position: absolute; left: 106px; top: 216px;
    font-weight: 600; font-size: 17px; letter-spacing: 3px;
    color: var(--slate);
  }
  .divider {
    position: absolute; left: 410px; top: 60px;
    width: 1.5px; height: 240px; background: var(--rule);
  }
  .contact { position: absolute; left: 440px; top: 62px; }
  .contact__name { font-weight: 600; font-size: 28px; color: var(--name); line-height: 1.2; }
  .contact__role { font-size: 25px; color: var(--ink); margin-bottom: 22px; }
  .contact__line {
    display: flex; align-items: center; gap: 10px;
    font-size: 21px; line-height: 1.5;
  }
  .contact__line svg { width: 18px; height: 18px; fill: var(--ink); }
  .contact__address { margin-bottom: 10px; }
</style>
</head>
<body>
  <main class="card">
    <svg class="card__swoosh" viewBox="0 0 900 530" aria-hidden="true">
      <path d="M0 332 C 220 382, 500 440, 700 530 L0 530 Z" fill="var(--slate)"/>
      <path d="M0 318 C 230 366, 520 424, 735 530" fill="none" stroke="var(--teal)" stroke-width="5"/>
    </svg>

    <div class="brand">
      <span class="brand__mark"></span>
      <span class="brand__name">KEYRISE</span>
    </div>
    <div class="brand__tagline">Property Investments</div>

    <div class="divider"></div>

    <section class="contact">
      <p class="contact__name">Marlow Ashby-Kent</p>
      <p class="contact__role">Consultant</p>
      <p class="contact__line contact__address">27, 9th Floor, Harbor Crest Road HCR</p>
      <p class="contact__line">
        <svg viewBox="0 0 24 24" aria-hidden="true"><path d="M6.6 10.8a15 15 0 0 0 6.6 6.6l2.2-2.2c.3-.3.7-.4 1-.2 1.1.4 2.3.6 3.6.6.6 0 1 .4 1 1V20c0 .6-.4 1-1 1A17 17 0 0 1 3 4c0-.6.4-1 1-1h3.5c.6 0 1 .4 1 1 0 1.3.2 2.5.6 3.6.1.3 0 .7-.2 1z"/></svg>
        020 555 0147
      </p>
      <p class="contact__line">
        <svg viewBox="0 0 24 24" aria-hidden="true"><path d="M6 3h9v5H6zM3 9h18v10H3zm4 3v2h4v-2zm0 3v2h10v-2z"/></svg>
        020 555 0148
      </p>
      <p class="contact__line">mail@keyrise.com</p>
      <p class="contact__line">www.keyrisebrokers.com</p>
    </section>
  </main>
</body>
</html>
```